Carpentry framing business card and logo design

We need a logo that works well with baseball caps, tee shirts and sweat shirts. We are a carpentry framing company specializing in apartment complexes and large residential communities. We work in what is known as the tri state area southeastern Pennsylvania , New Jersey and northern Delaware . We would like to see die signs using the old English letter M and royal blue colors. Also we stress WRSB compliance and safety.

Residential

Dalquist Construction Co Inc
1187 Harwick Lane
Brenford PA 19077
Rolf Dalquist
rolf1dalquist@quillmail.net
267-555-0148

```html
<!DOCTYPE html>
<html lang="en">
<head>
<meta charset="utf-8">
<title>Dalquist Construction Company Inc — Business Card</title>
<link rel="stylesheet" href="https://fonts.googleapis.com/css2?family=Arimo:wght@700&family=Tinos:wght@700&display=swap">
<style>
  :root {
    --navy: #2a4f86;
    --royal: #1a75bc;
    --paper: #ffffff;
  }
  html, body {
    margin: 0;
    padding: 0;
    width: 1200px;
    height: 701px;
    overflow: hidden;
    background: var(--paper);
  }
  .card {
    position: relative;
    width: 1200px;
    height: 701px;
    background: var(--paper);
    font-family: "Arimo", Arial, sans-serif;
    font-weight: 700;
  }
  .brand-mark {
    position: absolute;
    left: 44px;
    top: 135px;
    display: flex;
    align-items: center;
    gap: 18px;
    color: var(--royal);
    font-size: 72px;
    line-height: 1;
  }
  .brand-mark .dot {
    width: 44px;
    height: 44px;
    background: var(--royal);
  }
  .company-name {
    position: absolute;
    left: 394px;
    top: 49px;
    width: 756px;
    margin: 0;
    text-align: center;
    color: var(--navy);
    font-size: 56px;
    line-height: 53px;
    letter-spacing: 0.3px;
    white-space: nowrap;
  }
  .contact-person {
    position: absolute;
    left: 631px;
    top: 242px;
    margin: 0;
    color: var(--navy);
    font-size: 50px;
    line-height: 60px;
  }
  .address {
    position: absolute;
    left: 631px;
    top: 376px;
    margin: 0;
    font-style: normal;
    color: var(--royal);
    font-size: 42px;
    line-height: 52px;
  }
  .reach {
    position: absolute;
    left: 69px;
    top: 552px;
    margin: 0;
    color: var(--royal);
    font-size: 42px;
    line-height: 50px;
  }
  .tagline {
    position: absolute;
    left: 788px;
    top: 618px;
    margin: 0;
    color: var(--royal);
    font-family: "Tinos", "Times New Roman", serif;
    font-size: 23px;
    line-height: 23px;
    white-space: nowrap;
  }
</style>
</head>
<body>
  <main class="card">
    <div class="brand-mark">
      <span class="dot"></span>
      <span class="brand-name">Dalquist</span>
    </div>

    <h1 class="company-name">DALQUIST CONSTRUCTION<br>COMPANY INC</h1>

    <p class="contact-person">Rolf Dalquist<br>Owner</p>

    <address class="address">1187 Harwick Lane<br>Brenford PA 19077</address>

    <p class="reach">rolf1dalquist@quillmail.net<br>267-555-0148</p>

    <p class="tagline">WRSB Compliance And Safety 1st</p>
  </main>
</body>
</html>
```